Private Investigator needs business card with an intelligent logo

Private Investigator needs uncluttered, intelligently designed business card with simple logo. Prefer one or two colour print only. Must convey serious approach with only basic information: Business Name, "Clearwater Inquiries"
Phone: 03 4196 5031 Email: info@clear-water.example.com.au Web: www.clear-water.example.com.au
Agents Name: Gavin Thornley Title: Investigator Mobile: 0417 263 594

Thank you all very much for your designs.  There was some really excellent ideas and the choice was very hard.  I sought opinions from a number of people about which was the best one and there were a number of different choices but eventually the majority went with one design from Rovelko.  Thank you especially to those designers that made some changes when I suggested them.

Thanks again for all your efforts and good luck with your design careers.  I will certainly use SketchMarket again with the great quality of designers that made submissions.

Regards  Gavin Thornley

```html
<!DOCTYPE html>
<html lang="en">
<head>
<meta charset="utf-8">
<title>Clearwater Inquiries – Business Card</title>
<link rel="stylesheet" href="https://fonts.googleapis.com/css2?family=Cinzel:wght@400&family=Gelasio:wght@400;700&display=swap">
<style>
  :root {
    --backdrop: #e7e4df;
    --card: #fbfbf9;
    --ink: #2b2626;
    --rule: #3a3232;
    --print-grey: #a9a9ab;
  }
  * { margin: 0; padding: 0; box-sizing: border-box; }
  html, body {
    width: 1200px;
    height: 1000px;
    overflow: hidden;
    background: var(--backdrop);
  }
  .stage {
    width: 1200px;
    height: 1000px;
    display: flex;
    align-items: center;
    justify-content: center;
  }
  .business-card {
    position: relative;
    width: 900px;
    height: 550px;
    background: var(--card);
    box-shadow: 0 10px 30px rgba(0,0,0,0.12);
    color: var(--ink);
    overflow: hidden;
  }
  .company-name {
    position: absolute;
    top: 52px;
    left: 0;
    right: 0;
    text-align: center;
    font-family: "Cinzel", serif;
    font-size: 40px;
    letter-spacing: 1px;
    color: var(--ink);
  }
  .company-name .dot {
    display: inline-block;
    width: 8px;
    height: 8px;
    border-radius: 50%;
    background: var(--ink);
    vertical-align: middle;
    margin: 0 14px;
    position: relative;
    top: -3px;
  }
  .divider-rule {
    position: absolute;
    top: 156px;
    left: 0;
    width: 560px;
    height: 5px;
    background: var(--rule);
    border-radius: 0 3px 3px 0;
  }
  .agent {
    position: absolute;
    top: 118px;
    right: 40px;
    text-align: right;
  }
  .agent-name {
    font-family: "Gelasio", serif;
    font-weight: 700;
    font-size: 42px;
    line-height: 1;
    color: var(--ink);
  }
  .agent-title {
    font-family: "Gelasio", serif;
    font-size: 20px;
    margin-top: 2px;
    color: var(--ink);
  }
  .contact-list {
    position: absolute;
    top: 262px;
    right: 40px;
    text-align: right;
    list-style: none;
    font-family: "Gelasio", serif;
    font-size: 23px;
    line-height: 31px;
    color: var(--ink);
  }
  .fingerprint-mark {
    position: absolute;
    left: 40px;
    bottom: 26px;
    width: 96px;
    height: 120px;
  }
</style>
</head>
<body>
  <main class="stage">
    <article class="business-card">
      <h1 class="company-name"><span class="dot"></span>Clearwater Inquiries<span class="dot"></span></h1>
      <div class="divider-rule"></div>
      <div class="agent">
        <p class="agent-name">Gavin Thornley</p>
        <p class="agent-title">Investigator</p>
      </div>
      <ul class="contact-list">
        <li>Mobile: 0417 263 594</li>
        <li>Phone: 03 4196 5031</li>
        <li>Email: info@clear-water.example.com.au</li>
        <li>Web: www.clear-water.example.com.au</li>
      </ul>
      <svg class="fingerprint-mark" viewBox="0 0 96 120" role="img" aria-label="Grey fingerprint illustration">
        <defs>
          <radialGradient id="printTone" cx="50%" cy="50%" r="50%">
            <stop offset="0%" stop-color="#8f8f92"/>
            <stop offset="100%" stop-color="#c4c4c6"/>
          </radialGradient>
        </defs>
        <ellipse cx="48" cy="60" rx="44" ry="56" fill="url(#printTone)" opacity="0.8"/>
      </svg>
    </article>
  </main>
</body>
</html>
```